Business Cards/Stationery - Information Technology Company
Dale Porvin Advisory, An Information Technology Services Company
Business Cards/Stationery - Information Technology Company - Information Technology
Creative Brief
Use specific fonts
Whatever works the best.
Simple
Dale Porvin
Solutions Architect & Owner
928 Tarrow Street Suite 504 Glen Ellyn, IL 60139-8812
daleporvin@mailbright.example
http://daleporvin.example
Please use the tagline: "An Information Technology Services Company" under the logo on cards, letterhead, and envelope.
daleporvin daleporvin
Sorry about the long delay. I will be selecting a finalist in the next day.
The NPDX uses the bottom 1/2" of envelopes and prints a black barcode and text when processing. This area should be either be left blank or printed with very light colors or watermark. Designs can have printing on the bottom 1/2" of envelopes as long as it is light enough that NPDX can print its black barcode and it will be visible.
I will rate all designs very soon. Thanks for your patience.
QUIKMAKRR QUIKMAKRR
Star rating please,,,
The two color logo in .ai format has been uploaded and is now available to designers. Sorry about the delay.
The two logo in .ai format has been uploaded and is now available to designers. Sorry about the delay.
I really like the two sided designs that have been submitted so far. I didn't originally plan on a two sided design, but I have changed my mind thanks to all the designer's excellent work. PLEASE SUBMIT ALL FUTURE DESIGNS AS TWO SIDED. Thanks!
ninerock ninerock
Please upload Ai file of your logo!! thnks
I just uploaded the two color version of the logo in .jpg format. I also have .psd and .tif formats available. I don't have an .ai version, but I can get if needed. Please use the two color logo version and let me know if you need anything else. Thanks!

```html
<!DOCTYPE html>
<html lang="en">
<head>
<meta charset="utf-8">
<title>Dale Porvin Advisory — Business Card</title>
<link rel="stylesheet" href="https://fonts.googleapis.com/css2?family=Didact+Gothic&display=swap">
<style>
  :root {
    --backdrop: #2a2a2c;
    --card: #ffffff;
    --brand-blue: #1f6fc2;
    --text-grey: #5a5e63;
    --rule-blue: #3b82cf;
  }
  * { margin: 0; padding: 0; box-sizing: border-box; }
  html, body {
    width: 1200px; height: 901px; overflow: hidden;
    background: var(--backdrop);
    font-family: "Didact Gothic", Arial, sans-serif;
  }
  .card {
    position: absolute;
    width: 640px; height: 366px;
    background: var(--card);
    border-radius: 26px;
    box-shadow: 0 12px 30px rgba(0,0,0,0.45);
  }
  .card-back { left: 80px; top: 60px; }
  .card-front { left: 480px; top: 470px; }

  .back-mark {
    position: absolute; left: 50%; top: 50%;
    transform: translate(-50%, -50%);
    display: flex; align-items: center; gap: 12px;
    color: var(--brand-blue); font-size: 24px; white-space: nowrap;
  }
  .mark-square {
    width: 22px; height: 22px; background: var(--brand-blue); border-radius: 4px;
    flex: none;
  }

  .brand-block { position: absolute; left: 44px; top: 104px; }
  .brand-lockup { display: flex; align-items: center; gap: 14px; }
  .brand-name {
    color: var(--brand-blue); font-size: 33px; line-height: 1.0;
    border-left: 2px solid var(--rule-blue); padding-left: 12px;
  }
  .brand-tagline {
    margin-top: 10px; color: var(--text-grey); font-size: 11.5px; letter-spacing: 0.2px;
  }

  .contact-block { position: absolute; left: 392px; top: 106px; color: var(--text-grey); }
  .person-name { color: var(--brand-blue); font-size: 19px; }
  .person-title { font-size: 13px; margin-top: 2px; }
  .address { font-size: 13px; line-height: 1.35; margin-top: 12px; }
  .contact-lines { margin-top: 8px; font-size: 13px; line-height: 1.55; }
  .contact-line { display: flex; align-items: center; gap: 8px; }
  .contact-line svg { width: 11px; height: 11px; flex: none; }
</style>
</head>
<body>
  <section class="card card-back" aria-label="Card back">
    <div class="back-mark"><span class="mark-square"></span>Dale Porvin Advisory</div>
  </section>

  <section class="card card-front" aria-label="Card front">
    <div class="brand-block">
      <div class="brand-lockup">
        <span class="mark-square"></span>
        <div class="brand-name">Dale<br>Porvin<br>Advisory</div>
      </div>
      <div class="brand-tagline">An Information Technology Services Company</div>
    </div>

    <div class="contact-block">
      <div class="person-name">Dale Porvin</div>
      <div class="person-title">Solutions Architect &amp; Owner</div>
      <div class="address">928 Tarrow Street<br>Suite 504<br>Ferrow Bend, NE 68921-4410</div>
      <div class="contact-lines">
        <div class="contact-line">
          <svg viewBox="0 0 12 12"><path fill="#1f6fc2" d="M2 1h2l1 3-1.5 1a7 7 0 0 0 3.5 3.5L8 7l3 1v2a1 1 0 0 1-1 1A9 9 0 0 1 1 2a1 1 0 0 1 1-1z"/></svg>
          308-555-0184
        </div>
        <div class="contact-line">
          <svg viewBox="0 0 12 12"><rect x="0.5" y="2" width="11" height="8" rx="1" fill="#1f6fc2"/><path d="M1 3l5 4 5-4" stroke="#fff" fill="none"/></svg>
          daleporvin@mailbright.example
        </div>
        <div class="contact-line">
          <svg viewBox="0 0 12 12"><circle cx="6" cy="6" r="5.2" fill="none" stroke="#1f6fc2" stroke-width="1.2"/><path d="M1 6h10M6 1c-2.5 3-2.5 7 0 10M6 1c2.5 3 2.5 7 0 10" stroke="#1f6fc2" fill="none"/></svg>
          www.daleporvin.example
        </div>
      </div>
    </div>
  </section>
</body>
</html>
```